Flat pouch design for Fighting cock feed supplement

BRIEF:
* We need a pouch design for feed supplement for fighting cock.
* Designs for front and back packaging
DESIGN AND TASK DESCRIPTION
* brand name: BRV - Bravado Ridge Rooster
* product name: VIGRANOX
We are looking for a packaging design that caters to game fowl owners and enthusiasts. Our company is based here in the Philippines where fighting cock is a culture...
Our products must create a final packaging design impression of good quality, power and energy. all three elements must be emphasized and prominent. We would like you to have the liberty of choosing the colors to be used for as long as it does not go beyond or away from the whole "feel" and concept of the product.
The product will be presented in a 250 gram packaging and will be displayed on counters, product impression and being eye catching is important as most shops tend to be crowded.
Lastly, the Whole design for the packaging will also be used as base design and background for our other fighting cock products. Feel free to add tag lines to the product VIGRANOX.
Fighting Cock FYIs:
* comb and wattle are removed from the bird (these are removed from game cocks)
* Spur is on the left leg only
* Please refer to attached photos of cockfighting in action..
* you may Google fighting cocks in the Philippines for reference as different countries here in Asia have different styles of Fighting the birds.. Please Google "SABONG", it is a term used to fight cocks here in my country.
DIMENSIONS:
* 140mm x 230mm
NOTE:
* files added for reference and inspiration
* If you need other information for the product, kindly send us a message.
Thank You!
Colors
Designer to choose colors to be used in the design.
Look and feel

```html
<!DOCTYPE html>
<html lang="en">
<head>
<meta charset="utf-8">
<title>Bravado Ridge Rooster – Vigranox Pouch Range</title>
<link rel="stylesheet" href="https://fonts.googleapis.com/css2?family=Oswald:wght@300;500;700&family=Open+Sans:wght@400&display=swap">
<style>
  :root {
    --page-bg: #f4f4f4;
    --pouch-black: #050505;
    --panel-white: #ffffff;
    --header-white: #ffffff;
    --ink-dark: #141414;
    --variant-red: #e0151b;
    --variant-lime: #d9dc1f;
    --variant-lime-deep: #4d7a14;
    --variant-blue: #12aef0;
    --art-dark: #1b1b1b;
    --art-mid: #6a6a6a;
  }
  * { box-sizing: border-box; margin: 0; padding: 0; }
  html, body {
    width: 1200px;
    height: 900px;
    overflow: hidden;
    background: var(--page-bg);
  }
  .pouch-range {
    position: relative;
    width: 1200px;
    height: 900px;
    display: flex;
    justify-content: center;
    align-items: center;
    gap: 60px;
  }
  .pouch {
    position: relative;
    width: 300px;
    height: 493px;
    background: var(--pouch-black);
    box-shadow: 0 14px 30px rgba(0, 0, 0, 0.22);
  }
  .pouch--red  { --accent: var(--variant-red);  --accent-end: var(--variant-red); }
  .pouch--lime { --accent: var(--variant-lime); --accent-end: var(--variant-lime-deep); }
  .pouch--blue { --accent: var(--variant-blue); --accent-end: var(--variant-blue); }

  .pouch__tab {
    position: absolute;
    top: 0;
    left: 120px;
    width: 150px;
    height: 11px;
    background: var(--accent);
  }
  .pouch__brand {
    position: absolute;
    top: 18px;
    left: 0;
    width: 100%;
    text-align: center;
    color: var(--header-white);
    font-family: "Oswald", sans-serif;
    text-transform: uppercase;
    line-height: 1;
  }
  .pouch__brand-main {
    display: block;
    font-weight: 700;
    font-size: 32px;
    letter-spacing: 1px;
  }
  .pouch__brand-sub {
    display: block;
    font-weight: 700;
    font-size: 17px;
    letter-spacing: 1px;
    margin-top: 2px;
  }
  .pouch__panel {
    position: absolute;
    top: 88px;
    left: 58px;
    width: 184px;
    bottom: 14px;
    background: linear-gradient(to bottom,
      var(--panel-white) 0%,
      var(--panel-white) 30%,
      var(--accent) 62%,
      var(--accent-end) 100%);
    display: flex;
    flex-direction: column;
    align-items: center;
    padding: 14px 14px 0;
  }
  .pouch__art {
    width: 150px;
    height: 140px;
    border-radius: 50%;
    background: radial-gradient(circle at 50% 45%, var(--art-dark) 0%, var(--art-dark) 38%, var(--art-mid) 62%, rgba(255,255,255,0) 72%);
  }
  .pouch__variant {
    margin-top: 28px;
    font-family: "Oswald", sans-serif;
    font-weight: 500;
    font-size: 19px;
    color: var(--ink-dark);
    text-transform: uppercase;
    line-height: 1;
  }
  .pouch__product {
    font-family: "Oswald", sans-serif;
    font-weight: 300;
    font-size: 27px;
    color: var(--ink-dark);
    text-transform: uppercase;
    line-height: 1.05;
    letter-spacing: 0.5px;
  }
  .pouch__copy {
    margin-top: 16px;
    font-family: "Open Sans", sans-serif;
    font-size: 6.5px;
    line-height: 1.45;
    color: var(--ink-dark);
    text-align: justify;
  }
  .pouch--red .pouch__copy { color: #1a0000; }
</style>
</head>
<body>
  <main class="pouch-range">
    <article class="pouch pouch--red">
      <div class="pouch__tab"></div>
      <h1 class="pouch__brand"><span class="pouch__brand-main">Bravado</span><span class="pouch__brand-sub">Ridge Rooster</span></h1>
      <section class="pouch__panel">
        <div class="pouch__art" role="img" aria-label="Illustration of a black game rooster leaping with wings spread"></div>
        <h2 class="pouch__variant">Iron Strider</h2>
        <p class="pouch__product">Vigranox</p>
        <p class="pouch__copy">Daily feed supplement for game fowl. Supports stamina, muscle strength and fast recovery before and after training. Mix one scoop with regular feed each morning. Store in a cool dry place and reseal pouch after every use.</p>
      </section>
    </article>

    <article class="pouch pouch--lime">
      <div class="pouch__tab"></div>
      <h1 class="pouch__brand"><span class="pouch__brand-main">Bravado</span><span class="pouch__brand-sub">Ridge Rooster</span></h1>
      <section class="pouch__panel">
        <div class="pouch__art" role="img" aria-label="Illustration of a black game rooster leaping with wings spread"></div>
        <h2 class="pouch__variant">Iron Strider</h2>
        <p class="pouch__product">Vigranox</p>
        <p class="pouch__copy">Daily feed supplement for game fowl. Supports stamina, muscle strength and fast recovery before and after training. Mix one scoop with regular feed each morning. Store in a cool dry place and reseal pouch after every use.</p>
      </section>
    </article>

    <article class="pouch pouch--blue">
      <div class="pouch__tab"></div>
      <h1 class="pouch__brand"><span class="pouch__brand-main">Bravado</span><span class="pouch__brand-sub">Ridge Rooster</span></h1>
      <section class="pouch__panel">
        <div class="pouch__art" role="img" aria-label="Illustration of a black game rooster leaping with wings spread"></div>
        <h2 class="pouch__variant">Iron Strider</h2>
        <p class="pouch__product">Vigranox</p>
        <p class="pouch__copy">Daily feed supplement for game fowl. Supports stamina, muscle strength and fast recovery before and after training. Mix one scoop with regular feed each morning. Store in a cool dry place and reseal pouch after every use.</p>
      </section>
    </article>
  </main>
</body>
</html>
```